diesel mechanic business card design

stalwart diesel is a new and upcoming business we are looking for some bad ass designs to help get us started we offer 24 hour road service, off road recovery, welding and custom fabrications we are diesel mechanics so our design should be bold and eye catching flames wrenches engine parts are cool we work in an industrial environment around heavy trucks and equipment this in not a quikko slick we fix it all nothing is to big or to small the colors red and black are always a plus but we are open to anything you guys can come up with ready set go

Target Market(s)

other small business primarily trucking and transportation companys

Industry/Entity Type

Business

Contact Information for Business Card

company name Stalwert diesel truck & trailer repair / address 14 rear north benton ave taylor PA 18530 / ownersAdam DeLuccie 570-614-3385 / Curtis Vanholm 570-248-7731 E mail owenmarcotti@fieldpost.example fax 570-692-1856

Requirements
Nice to have
• industrial modern design
Should not have
• rainbows butterfly's unicorns or cupcakes

```html
<!DOCTYPE html>
<html lang="en">
<head>
<meta charset="utf-8">
<title>Stalwert Diesel Truck &amp; Trailer Repair — Business Card</title>
<link rel="stylesheet" href="https://fonts.googleapis.com/css2?family=Cinzel:wght@600&display=swap">
<style>
  :root {
    --paper: #ffffff;
    --leather-dark: #0f0b09;
    --leather-mid: #2a1c17;
    --band-red: rgba(120, 28, 18, 0.62);
    --band-edge: rgba(150, 140, 135, 0.35);
    --title-ink: #d9d6d3;
    --title-shadow: rgba(0, 0, 0, 0.75);
    --engine-warm: #b06a52;
    --engine-light: #d9c3b0;
  }
  * { margin: 0; padding: 0; box-sizing: border-box; }
  html, body {
    width: 1200px;
    height: 702px;
    overflow: hidden;
    background: var(--paper);
  }
  .card {
    position: absolute;
    left: 21px;
    top: 20px;
    width: 1162px;
    height: 660px;
    overflow: hidden;
    background: radial-gradient(ellipse at 45% 50%, var(--leather-mid) 0%, var(--leather-dark) 75%);
  }
  .leather-texture {
    position: absolute;
    inset: 0;
    background: linear-gradient(160deg, rgba(60,40,32,0.35), rgba(10,8,7,0.2) 60%, rgba(40,28,22,0.3));
  }
  .engine-art {
    position: absolute;
    left: 670px;
    top: 0;
    width: 492px;
    height: 660px;
  }
  .title-band {
    position: absolute;
    left: 0;
    top: 169px;
    width: 100%;
    height: 322px;
    background: var(--band-red);
    border-top: 9px solid var(--band-edge);
    border-bottom: 9px solid var(--band-edge);
  }
  .company-name {
    position: absolute;
    left: 36px;
    top: 10px;
    font-family: 'Cinzel', serif;
    font-weight: 600;
    color: var(--title-ink);
    text-shadow: 2px 3px 3px var(--title-shadow);
    font-size: 64px;
    line-height: 92px;
    letter-spacing: 0;
    white-space: nowrap;
  }
  .company-name .line { display: block; }
  .company-name .initial { font-size: 78px; }
</style>
</head>
<body>
  <main class="card">
    <div class="leather-texture" aria-hidden="true"></div>
    <svg class="engine-art" role="img" aria-label="Engine illustration with turbocharger and pulleys" viewBox="0 0 492 660">
      <defs>
        <radialGradient id="engineGlow" cx="0.5" cy="0.5" r="0.55">
          <stop offset="0" stop-color="#b06a52" stop-opacity="0.75"/>
          <stop offset="0.55" stop-color="#d9c3b0" stop-opacity="0.3"/>
          <stop offset="1" stop-color="#d9c3b0" stop-opacity="0"/>
        </radialGradient>
      </defs>
      <rect width="492" height="660" fill="url(#engineGlow)"/>
    </svg>
    <section class="title-band">
      <h1 class="company-name">
        <span class="line"><span class="initial">S</span>TALWERT</span>
        <span class="line">DIESEL TRUCK</span>
        <span class="line">&amp; TRAILER REPAIR</span>
      </h1>
    </section>
  </main>
</body>
</html>
```